Professional & attention grabbing.

A business card design, front and back. I already have a logo I will attach, but I am open to something new as well.
Things to include:
Name:
Title:
Phone:
Email:
Wanting something that is professional but attention grabbing.
Also we do a lot of work using drones on natural gas pipelines (leading the future)if you want to include any of that. I'm open to ideas.
Target Market(s)
Natural gas transmission industry / greenhouse gas mitigation industry
Industry/Entity Type
Business
Contact Information for Business Card
All details have been conveyed above.
Colors
Designer to choose colors to be used in the design.
Look and feel
Each slider illustrates characteristics of the customer's brand and the style your logo design should communicate.

```html
<!DOCTYPE html>
<html lang="en">
<head>
<meta charset="utf-8">
<title>Veyra Field Surveys – Business Card</title>
<link rel="stylesheet" href="https://fonts.googleapis.com/css2?family=Arimo:wght@400;700&family=Montserrat:wght@600;700&display=swap">
<style>
  :root {
    --stage: #a7a8ab;
    --card: #ffffff;
    --ink: #2f2f31;
    --maroon: #6b2f35;
    --brand-red: #c8202a;
    --gold-light: #f4d65c;
    --gold: #eebb33;
    --orange: #df8a2c;
  }
  * { margin: 0; padding: 0; box-sizing: border-box; }
  html, body { width: 1200px; height: 1200px; overflow: hidden; }
  body {
    position: relative;
    background: var(--stage);
    font-family: "Arimo", Arial, sans-serif;
    color: var(--ink);
  }
  .side-label {
    position: absolute;
    left: 80px;
    font-family: "Montserrat", Arial, sans-serif;
    font-weight: 700;
    font-size: 24px;
    letter-spacing: 4px;
    color: #111;
  }
  .side-label--front { top: 276px; }
  .side-label--back { top: 800px; }

  .card {
    position: absolute;
    left: 277px;
    width: 676px;
    height: 414px;
    background: var(--card);
  }
  .card--front { top: 108px; }
  .card--back { top: 618px; height: 417px; }

  .brand {
    position: absolute;
    left: 0; right: 0;
    top: 238px;
    display: flex;
    justify-content: center;
    align-items: center;
    gap: 14px;
  }
  .brand__mark {
    width: 40px; height: 40px;
    background: var(--brand-red);
  }
  .brand__name {
    font-family: "Arimo", Arial, sans-serif;
    font-weight: 700;
    font-size: 40px;
    color: var(--ink);
    letter-spacing: -0.5px;
  }
  .front-wave {
    position: absolute;
    left: 477px; top: 358px;
  }

  .holder {
    position: absolute;
    left: 0; right: 0;
    top: 684px;
    text-align: center;
  }
  .holder__name {
    font-family: "Arimo", Arial, sans-serif;
    font-weight: 700;
    font-size: 38px;
    color: var(--maroon);
    line-height: 1;
  }
  .holder__rule {
    width: 108px;
    height: 3px;
    background: var(--maroon);
    margin: 14px auto 12px;
  }
  .holder__title {
    font-size: 21px;
    color: var(--ink);
    letter-spacing: 0.5px;
  }

  .back-wave {
    position: absolute;
    left: 273px; top: 800px;
  }

  .contact {
    position: absolute;
    top: 893px;
    display: flex;
    align-items: center;
    gap: 22px;
    font-family: "Montserrat", Arial, sans-serif;
    font-weight: 700;
    font-size: 16px;
    letter-spacing: 2px;
    color: var(--ink);
  }
  .contact--phone { left: 365px; }
  .contact--email { left: 660px; }
</style>
</head>
<body>
  <div class="side-label side-label--front">FRONT</div>
  <div class="side-label side-label--back">BACK</div>

  <section class="card card--front" aria-label="Card front"></section>
  <div class="brand">
    <span class="brand__mark"></span>
    <span class="brand__name">Veyra Field Surveys</span>
  </div>
  <svg class="front-wave" width="266" height="40" viewBox="0 0 266 40" aria-hidden="true">
    <defs>
      <linearGradient id="frontWaveGrad" x1="0" x2="1" y1="0" y2="0">
        <stop offset="0" stop-color="#f4d65c"/>
        <stop offset="1" stop-color="#df8a2c"/>
      </linearGradient>
    </defs>
    <path d="M3,26 q16,-22 33,0 t33,0 t33,0 t33,0 t33,0 t33,0 t33,0 t33,0"
          fill="none" stroke="url(#frontWaveGrad)" stroke-width="6" stroke-linecap="round"/>
  </svg>

  <section class="card card--back" aria-label="Card back"></section>
  <div class="holder">
    <div class="holder__name">Name</div>
    <div class="holder__rule"></div>
    <div class="holder__title">TITLE</div>
  </div>

  <svg class="back-wave" width="760" height="235" viewBox="0 0 760 235" aria-hidden="true">
    <defs>
      <linearGradient id="bandGrad" x1="0" x2="1" y1="0" y2="0">
        <stop offset="0" stop-color="#f4d65c"/>
        <stop offset="0.45" stop-color="#eebb33"/>
        <stop offset="1" stop-color="#df8a2c"/>
      </linearGradient>
      <linearGradient id="backStrokeGrad" x1="0" x2="1" y1="0" y2="0">
        <stop offset="0" stop-color="#f0c843"/>
        <stop offset="1" stop-color="#e39433"/>
      </linearGradient>
      <clipPath id="cardClip">
        <rect x="4" y="0" width="676" height="235"/>
      </clipPath>
    </defs>
    <path clip-path="url(#cardClip)" fill="url(#bandGrad)"
      d="M0,26 q17,-22 34,0 t34,0 t34,0 t34,0 t34,0 t34,0 t34,0 t34,0 t34,0 t34,0 t34,0 t34,0 t34,0 t34,0 t34,0 t34,0 t34,0 t34,0 t34,0 t34,0 t34,0 t34,0 L748,235 L0,235 Z"/>
    <path fill="none" stroke="url(#backStrokeGrad)" stroke-width="6" stroke-linecap="round"
      d="M0,26 q17,-22 34,0 t34,0 t34,0 t34,0 t34,0 t34,0 t34,0 t34,0 t34,0 t34,0 t34,0 t34,0 t34,0 t34,0 t34,0 t34,0 t34,0 t34,0 t34,0 t34,0 t34,0 t34,0"/>
  </svg>

  <div class="contact contact--phone">
    <svg width="30" height="54" viewBox="0 0 30 54" aria-hidden="true">
      <rect x="2" y="2" width="26" height="46" rx="4" fill="none" stroke="#2f2f31" stroke-width="3"/>
      <rect x="6" y="8" width="18" height="32" fill="#f4d65c"/>
      <circle cx="15" cy="44" r="2" fill="#2f2f31"/>
    </svg>
    <span>+63 917 555 0142</span>
  </div>
  <div class="contact contact--email">
    <svg width="40" height="30" viewBox="0 0 40 30" aria-hidden="true">
      <rect x="1" y="1" width="38" height="28" rx="2" fill="#2f2f31"/>
      <path d="M2,3 L20,17 L38,3" fill="none" stroke="#eebb33" stroke-width="2"/>
    </svg>
    <span>hello@veyra.com</span>
  </div>
</body>
</html>
```